Stationary Set and Logo Update **PAYMENT GUARANTEED**

Stationery Design and Logo Update

About Us

Trindex Supply is a wholesale distributor of OEM [original brand] and compatible [generic brand] parts and supplies for use in copiers, faxes, printers, and multi-function machines. In plain English…we sell all the parts and supplies [such as toner] that make up any office equipment which outputs an image on paper.

Trindex was the 1st distributor to develop and sell a generic brand copier part in the United States. We have been in business since 1972 [nearly 40 years]. Our tagline is "The Steady Choice," as in our company was the first alternative product that copier dealers had to buying original brand copier parts. Trindex is known for offering reliable and cost-effective OEM and compatible products.

Project

We require a fresh, modern and corporate identity. Please submit a stationary package inclusive of a double-sided business card (2" x 3.5"), letterhead (8.5'x11"), and standard #10 envelope (4-1/8” x 9-1/2). You may use our current logo or preferably your take on an updated one. If an attempt is made in updating the logo #004D8E or a similar hue should be used as the primary color.

The design should be clean, simple, modern and professional and make an immediate impact.

Target Market(s)

Copier and printer dealers who lease and service imaging equipment in the United States and Latin America.

Industry/Entity Type

Business

Requirements
Must have
• Simple, clean, modern and professional. Please use #004D8E or a similar hue as the primary color. Letterhead must accommate (2) addresses. We have 2 locations.
Nice to have
• A simple, modern update to our current logo. https://assets.mailvorbo.example/fs030/5520384417702/img/418.jpg
Should not have
• More than (2) colors on logo.

```html
<!DOCTYPE html>
<html lang="en">
<head>
<meta charset="utf-8">
<title>Trindex Supply – Stationery Set</title>
<link rel="stylesheet" href="https://fonts.googleapis.com/css2?family=Arimo:wght@400;700&display=swap">
<style>
  :root {
    --paper: #ffffff;
    --page-bg: #ffffff;
    --edge: #d9dde0;
    --ink: #1f3440;
    --rule: #777777;
    --band-light: #4d6876;
    --band-mid: #0f2d39;
    --band-dark: #000000;
    --card-back: #0f2e3b;
    --band-line: #c6d2d8;
    --on-dark: #ffffff;
  }
  html, body {
    margin: 0;
    padding: 0;
    width: 967px;
    height: 1200px;
    overflow: hidden;
    background: var(--page-bg);
  }
  .stationery-set {
    display: block;
    width: 967px;
    height: 1200px;
  }
  .sheet { fill: var(--paper); stroke: var(--edge); stroke-width: 1; }
  .brand-dot { fill: var(--ink); }
  .brand-name { font-family: "Arimo", Arial, sans-serif; font-weight: 700; fill: var(--ink); }
  .address-rule { stroke: var(--rule); stroke-width: 0.8; }
  .band-rule { stroke: var(--band-line); stroke-width: 1; fill: none; }
  .band-text { font-family: "Arimo", Arial, sans-serif; fill: var(--on-dark); }
  .card-back-face { fill: var(--card-back); }
  .card-tile { fill: #ffffff; opacity: 0.07; }
  .card-divider { stroke: #ffffff; stroke-opacity: 0.3; stroke-width: 0.8; }
  .brand-name.reverse, .brand-dot.reverse { fill: var(--on-dark); }
</style>
</head>
<body>
<svg class="stationery-set" viewBox="0 0 900 1117" width="967" height="1200" role="group" aria-label="Trindex Supply stationery: envelope, letterhead and business card">
  <defs>
    <linearGradient id="band-gradient" x1="0" y1="0" x2="1" y2="0">
      <stop offset="0" stop-color="var(--band-light)"/>
      <stop offset="0.55" stop-color="var(--band-mid)"/>
      <stop offset="1" stop-color="var(--band-dark)"/>
    </linearGradient>
    <clipPath id="card-front-clip">
      <rect x="634" y="326" width="262" height="153" rx="14"/>
    </clipPath>
    <clipPath id="card-back-clip">
      <rect x="636" y="492" width="261" height="153" rx="12"/>
    </clipPath>
  </defs>

  <g class="envelope">
    <rect class="sheet" x="91" y="0.5" width="682" height="297"/>
    <g class="brand-lockup">
      <circle class="brand-dot" cx="116" cy="44" r="14"/>
      <text class="brand-name" x="138" y="58" font-size="38">Trindex</text>
    </g>
    <g class="recipient-lines">
      <line class="address-rule" x1="332" y1="115" x2="529" y2="115"/>
      <line class="address-rule" x1="332" y1="137" x2="529" y2="137"/>
      <line class="address-rule" x1="332" y1="159" x2="529" y2="159"/>
      <line class="address-rule" x1="332" y1="181" x2="529" y2="181"/>
    </g>
    <g class="footer-band">
      <path d="M91,192 Q330,242 773,190 L773,298 L91,298 Z" fill="url(#band-gradient)"/>
      <line class="band-rule" x1="91" y1="236" x2="773" y2="236"/>
      <line class="band-rule" x1="91" y1="284" x2="773" y2="284"/>
      <line class="band-rule" x1="261" y1="236" x2="261" y2="284"/>
      <line class="band-rule" x1="590" y1="236" x2="590" y2="284"/>
      <text class="band-text" font-size="8.2" text-anchor="middle">
        <tspan x="176" y="250">Corporate Office</tspan>
        <tspan x="176" y="261">2280 Harbor Pine Avenue</tspan>
        <tspan x="176" y="272">Millbrook, FL 33027</tspan>
      </text>
      <text class="band-text" x="426" y="264" font-size="10" text-anchor="middle">Toll Free: 800.555.0142</text>
      <text class="band-text" font-size="8.2" text-anchor="middle">
        <tspan x="685" y="247">West Coast Fulfillment Center</tspan>
        <tspan x="685" y="258">North Ridge Industrial Park #6</tspan>
        <tspan x="685" y="269">1740 Calder Way</tspan>
        <tspan x="685" y="280">Sparks, NV 89502</tspan>
      </text>
    </g>
  </g>

  <g class="letterhead">
    <rect class="sheet" x="0.5" y="325" width="613" height="791.5"/>
    <g class="brand-lockup">
      <circle class="brand-dot" cx="38" cy="382" r="15"/>
      <text class="brand-name" x="60" y="397" font-size="40">Trindex</text>
    </g>
    <g class="footer-band">
      <path d="M0,1018 Q250,1072 614,1012 L614,1117 L0,1117 Z" fill="url(#band-gradient)"/>
      <line class="band-rule" x1="0" y1="1057" x2="614" y2="1057"/>
      <line class="band-rule" x1="0" y1="1098" x2="614" y2="1098"/>
      <line class="band-rule" x1="0" y1="1109" x2="614" y2="1109"/>
      <line class="band-rule" x1="155" y1="1057" x2="155" y2="1098"/>
      <line class="band-rule" x1="450" y1="1057" x2="450" y2="1098"/>
      <text class="band-text" font-size="7.6" text-anchor="middle">
        <tspan x="77" y="1071">Corporate Office</tspan>
        <tspan x="77" y="1080">2280 Harbor Pine Avenue</tspan>
        <tspan x="77" y="1089">Millbrook, FL 33027</tspan>
      </text>
      <text class="band-text" x="305" y="1081" font-size="10" text-anchor="middle">Toll Free: 800.555.0142</text>
      <text class="band-text" font-size="7.6" text-anchor="middle">
        <tspan x="533" y="1068">West Coast Fulfillment Center</tspan>
        <tspan x="533" y="1077">North Ridge Industrial Park #6</tspan>
        <tspan x="533" y="1086">1740 Calder Way</tspan>
        <tspan x="533" y="1095">Sparks, NV 89502</tspan>
      </text>
    </g>
  </g>

  <g class="card-front">
    <rect class="sheet" x="634" y="326" width="262" height="153" rx="14"/>
    <g class="brand-lockup">
      <circle class="brand-dot" cx="663" cy="392" r="13"/>
      <text class="brand-name" x="683" y="405" font-size="35">Trindex</text>
    </g>
    <g class="footer-band" clip-path="url(#card-front-clip)">
      <path d="M634,440 Q760,456 896,420 L896,479 L634,479 Z" fill="url(#band-gradient)"/>
      <text class="band-text" x="768" y="466" font-size="9.5" text-anchor="middle">Toll Free: 800.555.0142</text>
    </g>
  </g>

  <g class="card-back">
    <g clip-path="url(#card-back-clip)">
      <rect class="card-back-face" x="636" y="492" width="261" height="153"/>
      <rect class="card-tile" x="851" y="492" width="46" height="46"/>
      <rect class="card-tile" x="806" y="544" width="44" height="44"/>
      <rect class="card-tile" x="852" y="544" width="45" height="44"/>
    </g>
    <text class="band-text" font-size="7.4">
      <tspan x="660" y="514">Corporate Office</tspan>
      <tspan x="660" y="524">2280 Harbor Pine Avenue</tspan>
      <tspan x="660" y="534">Millbrook, FL 33027</tspan>
      <tspan x="660" y="544">Local: 954.555.0183</tspan>
      <tspan x="660" y="554">Fax: 954.555.0190</tspan>
    </text>
    <line class="card-divider" x1="652" y1="569" x2="890" y2="569"/>
    <text class="band-text" font-size="7.4">
      <tspan x="660" y="586">West Coast Fulfillment Center</tspan>
      <tspan x="660" y="596">North Ridge Industrial Park #6</tspan>
      <tspan x="660" y="605">1740 Calder Way</tspan>
      <tspan x="660" y="615">Sparks, NV 89502</tspan>
      <tspan x="660" y="625">Fax: 775.555.0166</tspan>
    </text>
    <g class="brand-lockup">
      <circle class="brand-dot reverse" cx="825" cy="628" r="4.5"/>
      <text class="brand-name reverse" x="832" y="632" font-size="12">Trindex</text>
    </g>
  </g>
</svg>
</body>
</html>
```